Book Cover Design Project

Design a cover for a children's book. The book is both an educational tool and a Christian devotional. The subject of the book is the biography of Walter Brinkley and contains short descriptions of events from Brinkley's life as well as Christian devotions derived from those events. See attached back-cover material for more information.

Requirements
Must have
• 1. Red, White and Blue for colors.
2. The Tallow Creek Publishing logo which is attached in B&W or color.
3. Title "The Walter Brinkley Devotional: A Guide for Christian Learning"
4. Back cover material which is attached.

```html
<!DOCTYPE html>
<html lang="en">
<head>
<meta charset="utf-8">
<title>The Walter Brinkley Devotional</title>
<link rel="stylesheet" href="https://fonts.googleapis.com/css2?family=Arimo&family=Cabin+Condensed:wght@600&display=swap">
<style>
  :root {
    --cross-red: #e8000b;
    --paper: #ffffff;
    --ink: #111111;
    --flag-red: #c8102e;
    --flag-blue: #1c1f6e;
    --shadow: #555555;
    --portrait-dark: #2a1d14;
    --portrait-mid: #6b4a34;
    --portrait-light: #a98a6a;
    --imprint: #1f4e6b;
  }
  html, body { margin: 0; padding: 0; overflow: hidden; background: var(--paper); }
  .cover {
    position: relative;
    width: 849px;
    height: 1200px;
    background: var(--paper);
    overflow: hidden;
  }
  .cross-upright {
    position: absolute; left: 80px; top: 0;
    width: 154px; height: 1200px;
    background: var(--cross-red);
  }
  .cross-beam {
    position: absolute; left: 0; top: 195px;
    width: 849px; height: 152px;
    background: var(--cross-red);
  }
  .title {
    position: absolute; left: 40px; top: 242px;
    margin: 0;
    font-family: "Arimo", Arial, sans-serif;
    font-weight: 400;
    font-size: 40px;
    line-height: 1;
    color: var(--ink);
    white-space: nowrap;
  }
  .subtitle {
    position: absolute; right: 28px; top: 364px;
    margin: 0;
    font-family: "Cabin Condensed", sans-serif;
    font-weight: 600;
    font-size: 37px;
    letter-spacing: 0.5px;
    line-height: 1;
    color: var(--ink);
    white-space: nowrap;
  }
  .flag {
    position: absolute; left: 244px; top: 530px;
    width: 296px; height: 180px;
    box-shadow: 8px 8px 0 var(--shadow);
  }
  .flag svg { display: block; }
  .portrait {
    position: absolute; left: 535px; top: 710px;
    width: 293px; height: 178px;
    background:
      radial-gradient(ellipse 30% 45% at 72% 38%, var(--portrait-light), transparent 70%),
      linear-gradient(135deg, var(--portrait-mid) 0%, var(--portrait-dark) 65%, #1a120c 100%);
    box-shadow: 8px 8px 0 var(--shadow);
  }
  .imprint {
    position: absolute; right: 24px; top: 1118px;
    display: flex; align-items: center; gap: 12px;
  }
  .imprint-mark {
    width: 30px; height: 30px;
    background: var(--imprint);
  }
  .imprint-name {
    font-family: "Arimo", Arial, sans-serif;
    font-weight: 400;
    font-size: 26px;
    color: var(--imprint);
    white-space: nowrap;
  }
</style>
</head>
<body>
<main class="cover">
  <div class="cross-upright"></div>
  <div class="cross-beam"></div>
  <h1 class="title">The Walter Brinkley Devotional</h1>
  <h2 class="subtitle">A Guide for Christian Learning</h2>

  <div class="flag">
    <svg width="296" height="180" viewBox="0 0 296 180" aria-hidden="true">
      <rect width="296" height="180" fill="#ffffff"/>
      <g fill="var(--flag-red)">
        <rect y="0" width="296" height="13.85"/>
        <rect y="27.7" width="296" height="13.85"/>
        <rect y="55.4" width="296" height="13.85"/>
        <rect y="83.1" width="296" height="13.85"/>
        <rect y="110.8" width="296" height="13.85"/>
        <rect y="138.5" width="296" height="13.85"/>
        <rect y="166.15" width="296" height="13.85"/>
      </g>
      <rect width="118" height="97" fill="var(--flag-blue)"/>
      <g fill="#ffffff">
        <circle cx="10" cy="9" r="3"/><circle cx="30" cy="9" r="3"/><circle cx="50" cy="9" r="3"/><circle cx="70" cy="9" r="3"/><circle cx="90" cy="9" r="3"/><circle cx="108" cy="9" r="3"/>
        <circle cx="20" cy="19" r="3"/><circle cx="40" cy="19" r="3"/><circle cx="60" cy="19" r="3"/><circle cx="80" cy="19" r="3"/><circle cx="99" cy="19" r="3"/>
        <circle cx="10" cy="29" r="3"/><circle cx="30" cy="29" r="3"/><circle cx="50" cy="29" r="3"/><circle cx="70" cy="29" r="3"/><circle cx="90" cy="29" r="3"/><circle cx="108" cy="29" r="3"/>
        <circle cx="20" cy="39" r="3"/><circle cx="40" cy="39" r="3"/><circle cx="60" cy="39" r="3"/><circle cx="80" cy="39" r="3"/><circle cx="99" cy="39" r="3"/>
        <circle cx="10" cy="49" r="3"/><circle cx="30" cy="49" r="3"/><circle cx="50" cy="49" r="3"/><circle cx="70" cy="49" r="3"/><circle cx="90" cy="49" r="3"/><circle cx="108" cy="49" r="3"/>
        <circle cx="20" cy="59" r="3"/><circle cx="40" cy="59" r="3"/><circle cx="60" cy="59" r="3"/><circle cx="80" cy="59" r="3"/><circle cx="99" cy="59" r="3"/>
        <circle cx="10" cy="69" r="3"/><circle cx="30" cy="69" r="3"/><circle cx="50" cy="69" r="3"/><circle cx="70" cy="69" r="3"/><circle cx="90" cy="69" r="3"/><circle cx="108" cy="69" r="3"/>
        <circle cx="20" cy="79" r="3"/><circle cx="40" cy="79" r="3"/><circle cx="60" cy="79" r="3"/><circle cx="80" cy="79" r="3"/><circle cx="99" cy="79" r="3"/>
        <circle cx="10" cy="89" r="3"/><circle cx="30" cy="89" r="3"/><circle cx="50" cy="89" r="3"/><circle cx="70" cy="89" r="3"/><circle cx="90" cy="89" r="3"/><circle cx="108" cy="89" r="3"/>
      </g>
    </svg>
  </div>

  <div class="portrait" role="img" aria-label="Painted portrait of Walter Brinkley in a dark coat, standing before a red curtain and column"></div>

  <div class="imprint">
    <span class="imprint-mark"></span>
    <span class="imprint-name">Tallow Creek Publishing</span>
  </div>
</main>
</body>
</html>
```